" Visitamos clientes importadores e vendemos nossos servicos. Eles nos fornecem a factura a qual desejam importar e nos tratamos de todo o processo de desalfandegamento da mercadoria ate o transporte e entrega no armazem dos nossos clientes. "

```html
<!DOCTYPE html>
<html lang="pt-BR">
<head>
<meta charset="UTF-8">
<title>Assinatura de e-mail — Vértice Trading</title>
<link rel="stylesheet" href="https://fonts.googleapis.com/css2?family=Open+Sans:wght@400;600;700;800&display=swap">
<style>
  :root {
    --navy: #1d2a6b;
    --ink: #2b2b2b;
    --grey: #8a8f98;
    --rule: #c9ccd2;
    --card: #ffffff;
    --backdrop: #eceef0;
  }
  * { box-sizing: border-box; margin: 0; padding: 0; }
  html, body {
    width: 1200px; height: 1200px; overflow: hidden;
    background: var(--backdrop);
    font-family: "Open Sans", Arial, sans-serif;
  }
  .signature {
    position: absolute; left: 115px; top: 444px;
    width: 970px; height: 312px;
    background: var(--card);
  }
  .person-name {
    position: absolute; left: 74px; top: 40px;
    font-size: 35px; font-weight: 700; color: var(--navy);
    letter-spacing: -0.2px;
  }
  .name-rule {
    position: absolute; left: 72px; top: 91px; width: 327px; height: 2px;
    background: var(--navy);
  }
  .person-role {
    position: absolute; left: 74px; top: 101px;
    font-size: 21px; font-weight: 700; color: var(--ink);
  }
  .role-rule {
    position: absolute; left: 72px; top: 138px; width: 327px; height: 1px;
    background: var(--rule);
  }
  .contact-icon {
    position: absolute; width: 32px; height: 32px;
  }
  .icon-phone { left: 80px; top: 160px; }
  .icon-web { left: 80px; top: 227px; }
  .contact-lines {
    position: absolute; left: 136px;
    font-size: 21px; color: var(--ink); line-height: 27px;
  }
  .phones { top: 147px; }
  .web-lines { top: 216px; }
  .web-lines .site { font-weight: 700; color: var(--ink); }
  .social {
    position: absolute; left: 366px; top: 242px;
    display: flex; gap: 6px;
  }
  .social span {
    width: 19px; height: 19px; border-radius: 50%;
    background: var(--navy); display: block;
  }
  .divider {
    position: absolute; left: 463px; top: 31px; width: 2px; height: 252px;
    background: var(--grey);
  }
  .brand {
    position: absolute; left: 512px; top: 102px;
    display: flex; align-items: center; gap: 22px;
  }
  .brand-dot {
    width: 104px; height: 104px; border-radius: 50%;
    background: var(--navy);
  }
  .brand-text { display: flex; flex-direction: column; }
  .brand-name {
    font-size: 44px; font-weight: 800; color: var(--navy);
    letter-spacing: 1px; line-height: 1; text-transform: uppercase;
  }
  .brand-tagline {
    margin-top: 10px;
    font-size: 12px; font-weight: 400; color: var(--navy);
    letter-spacing: 0.6px; text-transform: uppercase;
  }
</style>
</head>
<body>
  <section class="signature">
    <h1 class="person-name">Nome Sobrenome</h1>
    <div class="name-rule"></div>
    <p class="person-role">Cargo Nome</p>
    <div class="role-rule"></div>

    <svg class="contact-icon icon-phone" viewBox="0 0 24 24" aria-hidden="true">
      <circle cx="12" cy="12" r="11" fill="none" stroke="#2b2b2b" stroke-width="1.6"/>
      <path d="M8.6 6.8c.4-.3 1-.2 1.2.2l1 2c.2.4.1.8-.2 1.1l-.7.6c.6 1.3 1.6 2.3 2.9 2.9l.6-.7c.3-.3.7-.4 1.1-.2l2 1c.4.2.5.8.2 1.2l-.8 1c-.5.6-1.3.8-2 .5-3-1.2-5.3-3.5-6.5-6.5-.3-.7-.1-1.5.5-2z" fill="#2b2b2b"/>
    </svg>
    <div class="contact-lines phones">
      <p>+ 55 00 90000 0000</p>
      <p>+ 55 00 0000 0000</p>
    </div>

    <svg class="contact-icon icon-web" viewBox="0 0 24 24" aria-hidden="true">
      <g fill="none" stroke="#1d2a6b" stroke-width="1.6">
        <circle cx="12" cy="12" r="10"/>
        <ellipse cx="12" cy="12" rx="4.5" ry="10"/>
        <path d="M2 12h20M4 6.5h16M4 17.5h16"/>
      </g>
    </svg>
    <div class="contact-lines web-lines">
      <p>contato@site.com.br</p>
      <p class="site">www.site.com.br</p>
    </div>
    <div class="social" aria-label="Redes sociais"><span></span><span></span></div>

    <div class="divider"></div>

    <div class="brand">
      <div class="brand-dot"></div>
      <div class="brand-text">
        <p class="brand-name">Vértice Trading</p>
        <p class="brand-tagline">Despachos aduaneiros e transporte</p>
      </div>
    </div>
  </section>
</body>
</html>
```